Premium men's gut health supplement needs a bottle label designed

We’re velnora - a premium men’s wellness brand focused on gut health. Our first product is a high-quality daily supplement designed to support digestion, regularity, and internal cleanliness. Backed by science and tailored for modern lifestyles, velnora is crafted in the UK and proudly LGBT-owned. It aims to resolve intimacy problems that gay men may experience due to poor digestion but also does not exclude any other orientation - other men may use it simply to improve their digestion.

velnora is for health-conscious men who value science-backed supplements and want to feel confident from the inside out. Many of our early adopters will be gay and bisexual men who prioritise gut health as part of their self-care, sexual, and hygiene routine, though the product is equally effective and appealing to anyone seeking premium digestive support.

The product is premium the target customer is male, not specific to one location but primary markets will be US, UK and EU.

I’d like a supplement bottle designed for velnora, our premium men’s gut health brand. The focus should be clean, slightly clinical, and minimal - inspired by brands like Quelrin and Darvo. The key element is the wordmark (velnora) on the front, with no additional logo or icon. Lowercase text and a strong, contemporary font are preferred.

The bottle should be aesthetically pleasing so that people are proud to display it on their shelf, instead of hiding it in a cupboard (like Quelrin, darvo, Pia Venturek, Morvanel etc)

Avoid anything that shows the product as being for LGBT, e.g., no rainbows, men holding hands etc.

The design should be premium, minimalist and not be busy or overwhelming.

I have uploaded a file called "Bottle" to give an idea of the type of container, but please ignore the colours and change as you see fit. This is just for reference for the type of bottle we'll use - all colours are customisable.

I have also uploaded some images for "style" reference, e.g., darvo, quelrin, pia venturek, etc for inspiration.

```html
<!DOCTYPE html>
<html lang="en">
<head>
<meta charset="utf-8">
<title>velnora digestive support — label colourways</title>
<link href="https://fonts.googleapis.com/css2?family=EB+Garamond:wght@600&family=Montserrat:wght@300;600&display=swap" rel="stylesheet">
<style>
  :root {
    --page: #ffffff;
    --ink-light: #f4f1ec;
    --amber-dark: #3e1a10;
    --amber-mid: #6b3420;
    --black-edge: #4a4a4a;
    --black-core: #070707;
    --taupe-edge: #bba796;
    --taupe-core: #94806d;
    --olive-edge: #a9ad78;
    --olive-core: #6a7030;
    --teal-edge: #7fa5ae;
    --teal-core: #235f6e;
  }
  * { box-sizing: border-box; margin: 0; padding: 0; }
  html, body { width: 1200px; height: 1200px; overflow: hidden; background: var(--page); }
  .range {
    position: relative;
    width: 1200px;
    height: 1200px;
  }
  .label {
    position: absolute;
    width: 255px;
    height: 298px;
    color: var(--ink-light);
    text-align: center;
  }
  .label--amber { background: linear-gradient(90deg, var(--amber-mid), var(--amber-dark) 50%, var(--amber-mid)); }
  .label--black { background: linear-gradient(90deg, var(--black-edge), var(--black-core) 50%, var(--black-edge)); }
  .label--taupe { background: linear-gradient(90deg, var(--taupe-edge), var(--taupe-core) 50%, var(--taupe-edge)); }
  .label--olive { background: linear-gradient(90deg, var(--olive-edge), var(--olive-core) 50%, var(--olive-edge)); }
  .label--teal  { background: linear-gradient(90deg, var(--teal-edge), var(--teal-core) 50%, var(--teal-edge)); }

  .col-1 { left: 112px; } .col-2 { left: 462px; } .col-3 { left: 831px; }
  .row-1 { top: 233px; } .row-2 { top: 809px; }

  .wordmark {
    position: absolute; left: 0; right: 0; top: 12px;
    font-family: "EB Garamond", serif;
    font-weight: 600;
    font-size: 56px;
    letter-spacing: -1.5px;
    line-height: 1;
  }
  .product-name {
    position: absolute; left: 0; right: 0; top: 107px;
    font-family: "Montserrat", sans-serif;
    line-height: 0.95;
  }
  .product-name .strong { display: block; font-weight: 600; font-size: 23px; }
  .product-name .light  { display: block; font-weight: 300; font-size: 26px; letter-spacing: 0.5px; }
  .claim {
    position: absolute; left: 72px; top: 190px;
    width: 110px; height: 34px;
    border: 1px solid var(--ink-light);
    display: flex; align-items: center;
    padding-left: 4px;
  }
  .claim-icon {
    width: 18px; height: 24px;
    background: rgba(244, 241, 236, 0.35);
    flex: none;
  }
  .claim-text {
    font-family: "Montserrat", sans-serif;
    font-weight: 300;
    font-size: 13px;
    line-height: 1;
    letter-spacing: 0.6px;
    text-align: right;
    flex: 1;
    padding-right: 3px;
  }
  .net-weight {
    position: absolute; left: 0; right: 0; top: 268px;
    font-family: "Montserrat", sans-serif;
    font-weight: 300;
    font-size: 10.5px;
  }
</style>
</head>
<body>
<main class="range">
  <section class="label label--amber col-1 row-1" role="img" aria-label="Translucent amber label showing brown capsules inside the bottle">
    <div class="wordmark">velnora</div>
    <div class="product-name"><span class="strong">digestive</span><span class="light">support</span></div>
    <div class="claim"><span class="claim-icon" role="img" aria-label="stomach icon"></span><span class="claim-text">internal<br>cleanliness</span></div>
    <div class="net-weight">Net Weight: 60 Capsules</div>
  </section>

  <section class="label label--black col-2 row-1">
    <div class="wordmark">velnora</div>
    <div class="product-name"><span class="strong">digestive</span><span class="light">support</span></div>
    <div class="claim"><span class="claim-icon" role="img" aria-label="stomach icon"></span><span class="claim-text">internal<br>cleanliness</span></div>
    <div class="net-weight">Net Weight: 60 Capsules</div>
  </section>

  <section class="label label--black col-3 row-1">
    <div class="wordmark">velnora</div>
    <div class="product-name"><span class="strong">digestive</span><span class="light">support</span></div>
    <div class="claim"><span class="claim-icon" role="img" aria-label="stomach icon"></span><span class="claim-text">internal<br>cleanliness</span></div>
    <div class="net-weight">Net Weight: 60 Capsules</div>
  </section>

  <section class="label label--taupe col-1 row-2">
    <div class="wordmark">velnora</div>
    <div class="product-name"><span class="strong">digestive</span><span class="light">support</span></div>
    <div class="claim"><span class="claim-icon" role="img" aria-label="stomach icon"></span><span class="claim-text">internal<br>cleanliness</span></div>
    <div class="net-weight">Net Weight: 60 Capsules</div>
  </section>

  <section class="label label--olive col-2 row-2">
    <div class="wordmark">velnora</div>
    <div class="product-name"><span class="strong">digestive</span><span class="light">support</span></div>
    <div class="claim"><span class="claim-icon" role="img" aria-label="stomach icon"></span><span class="claim-text">internal<br>cleanliness</span></div>
    <div class="net-weight">Net Weight: 60 Capsules</div>
  </section>

  <section class="label label--teal col-3 row-2">
    <div class="wordmark">velnora</div>
    <div class="product-name"><span class="strong">digestive</span><span class="light">support</span></div>
    <div class="claim"><span class="claim-icon" role="img" aria-label="stomach icon"></span><span class="claim-text">internal<br>cleanliness</span></div>
    <div class="net-weight">Net Weight: 60 Capsules</div>
  </section>
</main>
</body>
</html>
```